Financial Services Postcard Design

Glen Ostrow, CPA
Financial Services
Accounting/Tax/Consulting
Services include but not limited to
Financial Statements
Tax Returns
CFO/Controller services
Budgeting and Forecasting
Cash Management
Payroll / AP/ AR
Insurance Analysis
Cost Analysis
Special projects

I need a postcard design for my new financial service company to assist businesses in the Orange County area of southern California. I'm looking for a warm but bright look to represent CPA with many years of Management experience with manufacturing companies that can relate to business issues and provide solutions for small business.

Accounting

```html
<!DOCTYPE html>
<html lang="en">
<head>
<meta charset="utf-8">
<title>Financial Services Postcard</title>
<link rel="stylesheet" href="https://fonts.googleapis.com/css2?family=Open+Sans:wght@400;600;700&display=swap">
<style>
  :root {
    --bg: #e4e4e2;
    --blue-dark: #0a5f8e;
    --blue-mid: #1a86bf;
    --blue-light: #2aa6dc;
    --navy: #2a2f6e;
    --swoosh: #7d93ad;
    --panel: #f2f2f2;
    --orange: #ee7c22;
    --ink: #1d1d1d;
    --grey-text: #7b7b7b;
    --name-blue: #2a6fb8;
    --white: #ffffff;
  }
  * { box-sizing: border-box; margin: 0; padding: 0; }
  html, body { width: 1016px; height: 1200px; overflow: hidden; }
  body { background: var(--bg); font-family: "Open Sans", Arial, sans-serif; position: relative; }

  .postcard {
    position: absolute; width: 710px; height: 511px; background: var(--white);
    box-shadow: 0 3px 10px rgba(0,0,0,0.25); overflow: hidden;
  }
  .postcard--front { left: 104px; top: 67px; }
  .postcard--back { left: 180px; top: 623px; }

  .header { position: absolute; left: 0; top: 0; width: 710px; height: 140px; }
  .header svg { position: absolute; inset: 0; }
  .header__title {
    position: absolute; left: 0; right: 0; top: 18px; text-align: center;
    color: var(--white); font-weight: 700; font-size: 33px; line-height: 1.2;
  }
  .header__tagline {
    position: absolute; left: 0; right: 0; top: 62px; text-align: center;
    color: var(--white); font-size: 23px; letter-spacing: 1.5px; word-spacing: 2px;
  }
  .header__dot { display: inline-block; width: 8px; height: 8px; background: var(--white); margin: 0 10px 5px 12px; vertical-align: middle; }

  .footer-band {
    position: absolute; left: 0; bottom: 0; width: 100%; height: 25px;
    background: linear-gradient(90deg, var(--blue-light), #2c6aa6 45%, var(--navy));
  }

  .hero-photo {
    position: absolute; left: 0; top: 118px; width: 418px; height: 368px;
    background: linear-gradient(135deg, #c9d8e8 0%, #e7eef6 45%, #b4c7dc 100%);
  }
  .services-panel {
    position: absolute; left: 418px; top: 118px; width: 262px; height: 368px; background: var(--panel);
  }
  .services-heading {
    position: absolute; left: 412px; top: 149px; width: 276px; height: 43px;
    background: var(--orange); border-radius: 5px; color: var(--white);
    font-weight: 700; font-size: 17px; text-align: center; line-height: 43px;
  }
  .services-list { position: absolute; left: 433px; top: 212px; list-style: none; }
  .services-list li {
    font-size: 16.5px; color: var(--ink); line-height: 22.6px; display: flex; align-items: center;
  }
  .services-list svg { width: 13px; height: 13px; margin-right: 7px; flex: none; }
  .contact-line {
    position: absolute; left: 441px; top: 437px; font-size: 14px; color: var(--orange);
    display: flex; align-items: center;
  }
  .contact-line svg { width: 18px; height: 18px; margin: 0 7px 0 9px; }
  .contact-line strong { font-weight: 700; }

  .sender-panel {
    position: absolute; left: 0; top: 118px; width: 398px; height: 261px;
    background: var(--panel); border: 1px solid #c9c9c9; border-top: none; border-left: none;
    border-bottom-right-radius: 8px;
  }
  .portrait {
    position: absolute; left: 32px; top: 204px; width: 115px; height: 144px; border-radius: 3px;
    background: linear-gradient(180deg, #e9e2cf 0%, #cfb9a4 45%, #2a2c34 100%);
  }
  .sender-name { position: absolute; left: 177px; top: 208px; font-size: 16.5px; color: var(--name-blue); }
  .sender-detail {
    position: absolute; left: 173px; display: flex; font-size: 14px; color: var(--grey-text); line-height: 19px;
  }
  .sender-detail svg { width: 12px; height: 12px; margin: 3px 10px 0 0; flex: none; }
  .sender-detail--address { top: 235px; }
  .sender-detail--phone { top: 289px; }
  .sender-detail--email { top: 326px; }

  .stamp-box { position: absolute; left: 603px; top: 144px; width: 55px; height: 44px; border: 1px solid #9a9a9a; }
  .address-line { position: absolute; left: 488px; width: 168px; height: 1px; background: #8a8a8a; }
</style>
</head>
<body>

<section class="postcard postcard--front" aria-label="Postcard front">
  <div class="hero-photo" role="img" aria-label="Photo of coins, a calculator, a fountain pen and a printed table of figures"></div>
  <div class="services-panel"></div>

  <header class="header">
    <svg width="710" height="140" viewBox="0 0 710 140">
      <defs>
        <linearGradient id="hdrFront" x1="0" y1="0" x2="0" y2="1">
          <stop offset="0" stop-color="#2aa6dc"/>
          <stop offset="1" stop-color="#0a5f8e"/>
        </linearGradient>
      </defs>
      <path d="M0 0 H710 V120 Q420 150 0 110 Z" fill="url(#hdrFront)"/>
      <path d="M0 86 Q160 108 420 134 Q210 132 0 120 Z" fill="#7d93ad"/>
    </svg>
    <h1 class="header__title">Financial Services</h1>
    <p class="header__tagline">Accounting<span class="header__dot"></span>Tax<span class="header__dot"></span>Consulting</p>
  </header>

  <div class="services-heading">Our Services:</div>
  <ul class="services-list">
    <li><svg viewBox="0 0 14 14"><circle cx="7" cy="7" r="7" fill="#ee7c22"/><path d="M5.5 4 L8.5 7 L5.5 10" stroke="#fff" stroke-width="1.8" fill="none"/></svg>Financial Statements</li>
    <li><svg viewBox="0 0 14 14"><circle cx="7" cy="7" r="7" fill="#ee7c22"/><path d="M5.5 4 L8.5 7 L5.5 10" stroke="#fff" stroke-width="1.8" fill="none"/></svg>Tax Returns</li>
    <li><svg viewBox="0 0 14 14"><circle cx="7" cy="7" r="7" fill="#ee7c22"/><path d="M5.5 4 L8.5 7 L5.5 10" stroke="#fff" stroke-width="1.8" fill="none"/></svg>CFO/Controller services</li>
    <li><svg viewBox="0 0 14 14"><circle cx="7" cy="7" r="7" fill="#ee7c22"/><path d="M5.5 4 L8.5 7 L5.5 10" stroke="#fff" stroke-width="1.8" fill="none"/></svg>Budgeting and Forecasting</li>
    <li><svg viewBox="0 0 14 14"><circle cx="7" cy="7" r="7" fill="#ee7c22"/><path d="M5.5 4 L8.5 7 L5.5 10" stroke="#fff" stroke-width="1.8" fill="none"/></svg>Cash Management</li>
    <li><svg viewBox="0 0 14 14"><circle cx="7" cy="7" r="7" fill="#ee7c22"/><path d="M5.5 4 L8.5 7 L5.5 10" stroke="#fff" stroke-width="1.8" fill="none"/></svg>Payroll / AP/ AR</li>
    <li><svg viewBox="0 0 14 14"><circle cx="7" cy="7" r="7" fill="#ee7c22"/><path d="M5.5 4 L8.5 7 L5.5 10" stroke="#fff" stroke-width="1.8" fill="none"/></svg>Insurance Analysis</li>
    <li><svg viewBox="0 0 14 14"><circle cx="7" cy="7" r="7" fill="#ee7c22"/><path d="M5.5 4 L8.5 7 L5.5 10" stroke="#fff" stroke-width="1.8" fill="none"/></svg>Cost Analysis</li>
    <li><svg viewBox="0 0 14 14"><circle cx="7" cy="7" r="7" fill="#ee7c22"/><path d="M5.5 4 L8.5 7 L5.5 10" stroke="#fff" stroke-width="1.8" fill="none"/></svg>Special projects</li>
  </ul>
  <p class="contact-line">Contact Us
    <svg viewBox="0 0 20 20"><circle cx="10" cy="10" r="8.5" fill="none" stroke="#ee7c22" stroke-width="1.5"/><path d="M7 5.5 C6 6.5 6 8.5 8 11 C10 13.5 12.5 14.5 14 13.5 L12.6 11.8 L11.3 12.4 C10.3 11.9 8.8 10.2 8.3 9 L9 7.8 Z" fill="#ee7c22"/></svg>
    <strong>714-555-0142</strong></p>

  <div class="footer-band"></div>
</section>

<section class="postcard postcard--back" aria-label="Postcard back">
  <div class="sender-panel"></div>

  <header class="header">
    <svg width="710" height="140" viewBox="0 0 710 140">
      <defs>
        <linearGradient id="hdrBack" x1="0" y1="0" x2="0" y2="1">
          <stop offset="0" stop-color="#2aa6dc"/>
          <stop offset="1" stop-color="#0a5f8e"/>
        </linearGradient>
      </defs>
      <path d="M0 0 H710 V120 Q420 150 0 110 Z" fill="url(#hdrBack)"/>
      <path d="M0 86 Q160 108 420 134 Q210 132 0 120 Z" fill="#7d93ad"/>
    </svg>
    <h2 class="header__title">Financial Services</h2>
    <p class="header__tagline">Accounting<span class="header__dot"></span>Tax<span class="header__dot"></span>Consulting</p>
  </header>

  <div class="portrait" role="img" aria-label="Portrait photo of the accountant in a suit and tie"></div>
  <p class="sender-name">Glen Ostrow, CPA</p>
  <p class="sender-detail sender-detail--address">
    <svg viewBox="0 0 12 12"><path d="M6 0.5 C3.8 0.5 2.5 2 2.5 3.8 C2.5 6.5 6 11.5 6 11.5 C6 11.5 9.5 6.5 9.5 3.8 C9.5 2 8.2 0.5 6 0.5 Z" fill="#9a9a9a"/></svg>
    <span>275 N Willowbrook Ln.<br>Tustin, Ca. 92780</span></p>
  <p class="sender-detail sender-detail--phone">
    <svg viewBox="0 0 12 12"><path d="M2.5 0.8 C1.2 2 1.2 4.5 3.8 7.7 C6.3 10.8 9 11.6 10.8 10.5 L9.2 8.4 L7.7 9 C6.5 8.4 4.7 6.4 4.1 5 L5 3.5 Z" fill="#9a9a9a"/></svg>
    <span>714-555-0142</span></p>
  <p class="sender-detail sender-detail--email">
    <svg viewBox="0 0 12 12"><rect x="0.5" y="2.5" width="11" height="7" fill="#9a9a9a"/><path d="M0.5 2.5 L6 6.5 L11.5 2.5" stroke="#f2f2f2" stroke-width="1" fill="none"/></svg>
    <span>GlenOstrow@mailbox.net</span></p>

  <div class="stamp-box"></div>
  <div class="address-line" style="top:238px"></div>
  <div class="address-line" style="top:269px"></div>
  <div class="address-line" style="top:300px"></div>

  <div class="footer-band"></div>
</section>

</body>
</html>
```